Business card design for engineering firm specializing in defense industry.

We need a professional business card design. Something simple but stands out. We are an engineering company specializing in composites in the defense industry.
Industry/Entity Type
Defense
Contact Information for Business Card
A simple black business card with the Varlonix yellow color is what we had in mind but open for other designs.
Colors
ffc214

```html
<!DOCTYPE html>
<html lang="en">
<head>
<meta charset="utf-8">
<title>Varlonix — Business Card</title>
<link rel="stylesheet" href="https://fonts.googleapis.com/css2?family=Montserrat:wght@500;800&display=swap">
<style>
  :root {
    --backdrop: #3b3b3c;
    --card-black: #231f20;
    --brand-yellow: #ffc214;
    --brand-amber: #f7a21b;
    --brand-orange: #ef8a22;
    --deep-orange: #d8702a;
    --text-light: #e9e6e1;
    --name-white: #ffffff;
  }
  * { box-sizing: border-box; margin: 0; padding: 0; }
  html, body {
    width: 1200px; height: 1200px; overflow: hidden;
    background: var(--backdrop);
    font-family: "Montserrat", Arial, sans-serif;
  }
  .canvas {
    width: 1200px; height: 1200px;
    display: flex; flex-direction: column; align-items: center;
    justify-content: center; gap: 54px;
  }
  .card {
    position: relative;
    width: 880px; height: 503px;
    background: var(--card-black);
    overflow: hidden;
    box-shadow: 0 18px 40px rgba(0,0,0,.35);
  }
  .card-art { position: absolute; inset: 0; width: 100%; height: 100%; }
  .brand {
    position: absolute;
    display: flex; align-items: center; gap: 16px;
  }
  .brand-mark {
    width: 22px; height: 22px; border-radius: 50%;
    background: var(--brand-yellow);
  }
  .brand-name {
    font-weight: 800; font-size: 64px; letter-spacing: 1px;
    color: var(--name-white); line-height: 1;
  }
  .front .brand { left: 120px; top: 205px; }
  .back .brand { left: 200px; top: 178px; }
  .contact-list {
    position: absolute; right: 48px; top: 92px;
    list-style: none;
    display: flex; flex-direction: column; gap: 26px;
  }
  .contact-item {
    display: flex; align-items: center; justify-content: flex-end; gap: 22px;
    font-weight: 500; font-size: 17px; color: var(--text-light);
  }
  .contact-icon { width: 34px; height: 34px; flex: none; }
</style>
</head>
<body>
<main class="canvas">

  <section class="card front" aria-label="Card front">
    <svg class="card-art" viewBox="0 0 880 503" aria-hidden="true">
      <defs>
        <linearGradient id="wave-outer" x1="0" y1="1" x2="1" y2="0">
          <stop offset="0" stop-color="#ffc214"/>
          <stop offset="1" stop-color="#f39a1c"/>
        </linearGradient>
        <linearGradient id="wave-inner" x1="0" y1="0.5" x2="1" y2="0.5">
          <stop offset="0" stop-color="#f7a21b"/>
          <stop offset="1" stop-color="#d8702a"/>
        </linearGradient>
      </defs>
      <path d="M120,503 C400,470 440,110 880,60 L880,503 Z" fill="url(#wave-outer)"/>
      <path d="M170,503 C440,455 500,170 880,118 L880,503 Z" fill="var(--card-black)"/>
      <path d="M205,503 C470,455 530,200 880,150 L880,503 Z" fill="url(#wave-outer)"/>
      <path d="M250,503 C500,460 560,235 880,200 L880,503 Z" fill="var(--card-black)"/>
      <path d="M320,503 C560,450 620,280 880,250 L880,503 Z" fill="url(#wave-inner)"/>
    </svg>
    <div class="brand">
      <span class="brand-mark"></span>
      <span class="brand-name">Varlonix</span>
    </div>
  </section>

  <section class="card back" aria-label="Card back">
    <svg class="card-art" viewBox="0 0 880 503" aria-hidden="true">
      <defs>
        <linearGradient id="corner-fill" x1="0" y1="1" x2="1" y2="0">
          <stop offset="0" stop-color="#ffc214"/>
          <stop offset="0.6" stop-color="#f39a1c"/>
          <stop offset="1" stop-color="#e8832a"/>
        </linearGradient>
      </defs>
      <path d="M0,0 L230,0 C120,60 80,250 330,300 C470,330 560,360 640,503 L0,503 Z" fill="url(#corner-fill)"/>
      <path d="M195,0 L230,0 C120,60 80,250 330,300 C470,330 560,360 640,503 L610,503 C540,390 450,345 320,320 C60,270 70,70 195,0 Z" fill="var(--card-black)"/>
      <path d="M150,0 L195,0 C70,70 60,270 320,320 C450,345 540,390 610,503 L575,503 C500,410 420,370 300,345 C20,290 20,80 150,0 Z" fill="#f7a21b"/>
    </svg>
    <div class="brand">
      <span class="brand-mark"></span>
      <span class="brand-name">Varlonix</span>
    </div>
    <ul class="contact-list">
      <li class="contact-item">
        <span>your address</span>
        <svg class="contact-icon" viewBox="0 0 34 34" aria-hidden="true">
          <circle cx="17" cy="17" r="17" fill="var(--brand-yellow)"/>
          <path d="M17,8 a6,6 0 0 1 6,6 c0,5 -6,11 -6,11 s-6,-6 -6,-11 a6,6 0 0 1 6,-6 z" fill="var(--card-black)"/>
          <circle cx="17" cy="14" r="2.2" fill="var(--brand-yellow)"/>
        </svg>
      </li>
      <li class="contact-item">
        <span>01234 567890</span>
        <svg class="contact-icon" viewBox="0 0 34 34" aria-hidden="true">
          <circle cx="17" cy="17" r="17" fill="var(--brand-yellow)"/>
          <path d="M12,9 l3,0 l1.5,4 l-2,1.5 c1,2.5 2.5,4 5,5 l1.5,-2 l4,1.5 l0,3 c-8,1 -14,-5 -13,-13 z" fill="var(--card-black)"/>
        </svg>
      </li>
      <li class="contact-item">
        <span>www.yourwebsite.com</span>
        <svg class="contact-icon" viewBox="0 0 34 34" aria-hidden="true">
          <circle cx="17" cy="17" r="17" fill="var(--brand-yellow)"/>
          <g fill="none" stroke="var(--card-black)" stroke-width="1.8">
            <circle cx="17" cy="17" r="8"/>
            <ellipse cx="17" cy="17" rx="3.5" ry="8"/>
            <line x1="9" y1="17" x2="25" y2="17"/>
          </g>
        </svg>
      </li>
    </ul>
  </section>

</main>
</body>
</html>
```